"Harrow Crest Builders" is a residential building company and needs a new business card design and may re

We would like a redesign based on the existing logo, and would like to see a new font as well. We are bespoke home builders who build sustainable energy efficient homes.

Industry/Entity Type

Construction

Contact Information for Business Card

Business card size 40mm x 90mm

Colors

Designer to choose colors to be used in the design.

```html
<!DOCTYPE html>
<html lang="en">
<head>
<meta charset="utf-8">
<title>Harrow Crest Builders – Business Card</title>
<link rel="stylesheet" href="https://fonts.googleapis.com/css2?family=Oswald:wght@400;500;600&display=swap">
<style>
  :root {
    --lime: #b3cc2e;
    --ink: #0d0d0d;
    --paper: #ffffff;
    --backdrop: #d9dadc;
    --text-dark: #1a1a1a;
  }
  * { box-sizing: border-box; margin: 0; padding: 0; }
  html, body { width: 1200px; height: 857px; overflow: hidden; }
  body {
    background: var(--backdrop);
    font-family: "Oswald", "Arial Narrow", sans-serif;
    display: flex;
    flex-direction: column;
    align-items: center;
    justify-content: center;
    gap: 44px;
  }
  .card {
    position: relative;
    width: 600px;
    height: 340px;
    overflow: hidden;
    box-shadow: 0 6px 18px rgba(0,0,0,0.18);
  }

  /* Front */
  .card--front { background: var(--paper); }
  .card__edge-left { position: absolute; left: 0; top: 0; bottom: 0; width: 14px; background: var(--lime); }
  .card__edge-right { position: absolute; right: 0; top: 0; bottom: 0; width: 14px; background: var(--ink); }
  .brand {
    position: absolute; left: 52px; top: 128px; width: 170px;
    display: flex; align-items: center; gap: 10px;
  }
  .brand__square { width: 22px; height: 22px; background: var(--lime); flex: none; }
  .brand__name {
    font-weight: 600; font-size: 20px; line-height: 1.1;
    letter-spacing: 1.5px; text-transform: uppercase; color: var(--ink);
  }
  .divider { position: absolute; left: 244px; top: 58px; width: 4px; height: 234px; background: var(--lime); }
  .holder {
    position: absolute; left: 272px; top: 58px;
    font-weight: 600; font-size: 30px; letter-spacing: 0.5px;
    text-transform: uppercase; color: var(--ink); line-height: 1;
  }
  .contact {
    position: absolute; left: 272px; top: 118px;
    display: flex; gap: 14px;
  }
  .contact__icons {
    width: 34px; background: var(--lime);
    display: flex; flex-direction: column; justify-content: space-around; align-items: center;
    padding: 8px 0; height: 156px;
  }
  .contact__icons svg { width: 18px; height: 18px; }
  .contact__lines {
    display: flex; flex-direction: column; justify-content: space-around; height: 156px;
    font-weight: 500; font-size: 13px; letter-spacing: 0.3px; text-transform: uppercase;
    color: var(--text-dark); line-height: 1.15;
  }

  /* Back */
  .card--back { background: var(--lime); }
  .card--back svg.card__bands { position: absolute; inset: 0; }
  .back-brand {
    position: absolute; left: 0; right: 0; top: 96px;
    display: flex; justify-content: center; align-items: center; gap: 16px;
  }
  .back-brand__square { width: 40px; height: 40px; background: var(--paper); flex: none; }
  .back-brand__name {
    font-weight: 600; font-size: 42px; letter-spacing: 3px; line-height: 1;
    text-transform: uppercase; color: var(--paper);
  }
  .back-web {
    position: absolute; left: 0; right: 0; bottom: 26px; text-align: center;
    font-weight: 500; font-size: 15px; letter-spacing: 2.5px;
    text-transform: uppercase; color: var(--paper);
  }
</style>
</head>
<body>

  <section class="card card--back" aria-label="Business card back">
    <svg class="card__bands" width="600" height="340" viewBox="0 0 600 340" aria-hidden="true">
      <path d="M0 232 Q300 330 600 196 L600 340 L0 340 Z" fill="var(--ink)"/>
    </svg>
    <div class="back-brand">
      <span class="back-brand__square"></span>
      <span class="back-brand__name">Harrow Crest Builders</span>
    </div>
    <p class="back-web">www.harrowcrestbuilders.com.au</p>
  </section>

  <section class="card card--front" aria-label="Business card front">
    <span class="card__edge-left"></span>
    <span class="card__edge-right"></span>

    <div class="brand">
      <span class="brand__square"></span>
      <span class="brand__name">Harrow Crest Builders</span>
    </div>

    <span class="divider"></span>

    <h1 class="holder">Daniel Ferrante</h1>

    <div class="contact">
      <div class="contact__icons">
        <svg viewBox="0 0 24 24" aria-label="Address"><path d="M12 2a7 7 0 0 0-7 7c0 5 7 13 7 13s7-8 7-13a7 7 0 0 0-7-7zm0 9.5A2.5 2.5 0 1 1 12 6.5a2.5 2.5 0 0 1 0 5z" fill="#fff"/></svg>
        <svg viewBox="0 0 24 24" aria-label="Website"><g fill="none" stroke="#fff" stroke-width="2.6" stroke-linecap="round"><path d="M10 14l4-4"/><path d="M8.5 11.5l-2 2a3.2 3.2 0 0 0 4.5 4.5l2-2"/><path d="M15.5 12.5l2-2A3.2 3.2 0 0 0 13 6l-2 2"/></g></svg>
        <svg viewBox="0 0 24 24" aria-label="Phone"><path d="M6.6 10.8a15 15 0 0 0 6.6 6.6l2.2-2.2a1 1 0 0 1 1-.25 11.4 11.4 0 0 0 3.6.57 1 1 0 0 1 1 1V20a1 1 0 0 1-1 1A17 17 0 0 1 3 4a1 1 0 0 1 1-1h3.5a1 1 0 0 1 1 1c0 1.25.2 2.45.57 3.6a1 1 0 0 1-.25 1z" fill="#fff"/></svg>
        <svg viewBox="0 0 24 24" aria-label="Email"><path d="M3 6h18v12H3z" fill="#fff"/><path d="M3 6l9 7 9-7" fill="none" stroke="var(--lime)" stroke-width="2"/></svg>
      </div>
      <div class="contact__lines">
        <span>PO Box 4187 Eastgate LPO<br>Bellmont WA 6104</span>
        <span>www.harrowcrestbuilders.com.au</span>
        <span>0412 555 019</span>
        <span>daniel@harrowcrestbuilders.com.au</span>
      </div>
    </div>
  </section>

</body>
</html>
```